Eye-Catching, Direct Marketing Residential Painting Flyer!

I am run a residential painting business and am looking for a flyer to be designed to mailout to potential customers.
I want the copy/wording to be designed similar to this flyer.

It's important that the person reading the flyer gets the benefits we're promoting which is why I want the wording/copy to be almost identical to the flyer attached.

However, the structure will be different. The flyer will be a postcard thick, 5 x11.5.
Double sided.

The name of the company is Brightwall Coaters.

I would also like the prominent colour to either be light green or orange.

Target Market(s)

Home Owners between the age of 45-80.

Industry/Entity Type

Painting And Decorating

Font styles to use
Serif

Colors
f68d4d
faa54b
f78f20
f37122
9bcb3c
abd037
cadf82

Requirements
Must have
• Excellent Eye-Catching Design
• Benefits Visibly Promoted
• Action Taking Incentive- Call Now for FREE Window Cleaning and FREE Painting Estimate
Should not have
• Crowded wording

```html
<!DOCTYPE html>
<html lang="en">
<head>
<meta charset="utf-8">
<title>Brightwall Coaters – Flyer</title>
<link rel="stylesheet" href="https://fonts.googleapis.com/css2?family=Oswald:wght@600;700&family=Arimo:wght@700&family=Ubuntu:wght@500;700&family=Tinos&display=swap">
<style>
  :root {
    --stage: #ebe6df;
    --paper: #ffffff;
    --header-orange: #f37122;
    --brand-orange: #e8621c;
    --deep-orange: #d9541a;
    --deep-green: #5f8f17;
    --ink-brown: #4a2410;
    --ink: #231a1a;
    --accent-orange: #f78f20;
    --accent-green: #9bcb3c;
    --rule-green: #cadf82;
    --photo-light: #b59b7c;
    --photo-dark: #7a4a2c;
  }
  * { margin: 0; padding: 0; box-sizing: border-box; }
  html, body { width: 1200px; height: 1200px; overflow: hidden; }
  body { background: var(--stage); position: relative; }

  .flyer {
    position: absolute; left: 374px; top: 81px;
    width: 451px; height: 1038px;
    background: var(--paper);
    box-shadow: 0 6px 18px rgba(0,0,0,.25);
    overflow: hidden;
  }
  .flyer__art { position: absolute; inset: 0; }

  .header {
    position: absolute; left: 0; top: 0; width: 100%; height: 98px;
    background: var(--header-orange);
    display: flex; align-items: center; justify-content: center;
    text-align: center;
    font-family: "Oswald", sans-serif; font-weight: 700;
    font-size: 36px; line-height: 39px; color: #fff;
    text-shadow: 2px 2px 2px rgba(0,0,0,.4);
  }

  .brand {
    position: absolute; left: 0; top: 604px; width: 100%;
    text-align: center;
    font-family: "Arimo", sans-serif; font-weight: 700;
    font-size: 34px; color: var(--brand-orange); letter-spacing: -0.5px;
  }

  .tagline {
    position: absolute; left: 0; top: 664px; width: 100%;
    text-align: center;
    font-family: "Oswald", sans-serif; font-weight: 700;
    color: var(--deep-orange);
  }
  .tagline__lead { font-size: 27px; line-height: 34px; color: var(--deep-green); }
  .tagline__big { font-size: 37px; line-height: 42px; }
  .tagline__end { font-size: 24px; line-height: 30px; color: var(--deep-green); }

  .rule {
    position: absolute; left: 12px; width: 427px; height: 3px;
    background: linear-gradient(90deg, transparent, var(--rule-green) 20%, var(--rule-green) 80%, transparent);
  }
  .rule--top { top: 788px; }
  .rule--bottom { top: 958px; }

  .offer {
    position: absolute; left: 0; top: 794px; width: 100%;
    text-align: center;
    font-family: "Ubuntu", sans-serif; font-weight: 700;
    font-size: 27px; line-height: 37.5px; color: var(--ink);
  }
  .offer__call { color: var(--ink-brown); }
  .offer__free { color: var(--deep-orange); }
  .offer__amp { color: var(--deep-green); }

  .links {
    position: absolute; left: 0; top: 962px; width: 100%;
    text-align: center;
    font-family: "Tinos", serif; font-size: 25px; line-height: 32px;
    color: var(--ink-brown);
  }
</style>
</head>
<body>
  <main class="flyer">
    <svg class="flyer__art" width="451" height="1038" viewBox="0 0 451 1038">
      <defs>
        <linearGradient id="deckTone" x1="0" y1="0" x2="1" y2="0.6">
          <stop offset="0" stop-color="#b59b7c"/>
          <stop offset="0.55" stop-color="#a88a6a"/>
          <stop offset="1" stop-color="#7a4a2c"/>
        </linearGradient>
        <radialGradient id="figureTone" cx="0.5" cy="0.5" r="0.5">
          <stop offset="0" stop-color="#c9d6e2" stop-opacity="0.25"/>
          <stop offset="1" stop-color="#c9d6e2" stop-opacity="0"/>
        </radialGradient>
      </defs>
      <rect role="img" aria-label="Photo of a wooden deck half stained, with a can of stain, a brush and a pair of work gloves" x="0" y="98" width="451" height="470" fill="url(#deckTone)"/>
      <polygon class="wedge wedge--orange" points="0,440 178,562 0,504" fill="#f78f20"/>
      <polygon class="wedge wedge--green" points="451,384 266,562 451,528" fill="#9bcb3c"/>
      <polygon class="panel" points="0,504 182,562 218,570 266,562 451,528 451,1038 0,1038" fill="#ffffff"/>
      <rect role="img" aria-label="Faint illustration of a painter holding a paint brush" x="20" y="620" width="410" height="360" fill="url(#figureTone)"/>
      <circle class="badge" cx="225" cy="548" r="39" fill="#fff" stroke="#1a1a1a" stroke-width="7"/>
    </svg>

    <header class="header">Take control of how<br>your home looks!</header>

    <div class="brand">BRIGHTWALL COATERS</div>

    <div class="tagline">
      <div class="tagline__lead">We make your home look</div>
      <div class="tagline__big">CLEAN, FRESH &amp; Beautiful</div>
      <div class="tagline__end">again!</div>
    </div>

    <div class="rule rule--top"></div>

    <div class="offer">
      <div class="offer__call">Call Now for : 555-013-2748</div>
      <div><span class="offer__free">FREE</span> Window Cleaning</div>
      <div class="offer__amp">&amp;</div>
      <div><span class="offer__free">FREE</span> Painting Estimate</div>
    </div>

    <div class="rule rule--bottom"></div>

    <div class="links">
      <div>brightwallcoaters.com</div>
      <div>brightwallcoaters.com/community</div>
    </div>
  </main>
</body>
</html>
```